Brevane - Business Card Design

Design a modern masculine business card for our business

Target Market(s)

Private Market

Industry/Entity Type

Construction

Contact Information for Business Card

Company Name - Name of Person - Address - email address - contact number

Font styles to use
Serif
Sans Serif

Colors
0094D4
00A9DD
6FCCEA
C7EBF8
E9F6FB
00AB8E
00BBA5
67D7C9
C6EFE9
E9F9F6
F0912C
F2A743
F7CA91
FBE8D2
FDF5EE

Requirements
Must have
• Use company logo provided
Nice to have
• Company Logo

```html
<!DOCTYPE html>
<html lang="en">
<head>
<meta charset="utf-8">
<title>Brevane Business Card</title>
<link href="https://fonts.googleapis.com/css2?family=Montserrat:wght@300;400;700;800&display=swap" rel="stylesheet">
<style>
  :root {
    --bg: #e4e5e8;
    --ink: #111111;
    --paper: #ffffff;
    --accent: #f0722c;
    --muted: #555555;
    --shadow: rgba(0,0,0,0.18);
  }
  * { margin: 0; padding: 0; box-sizing: border-box; }
  html, body { width: 1200px; height: 800px; overflow: hidden; }
  body {
    background: var(--bg);
    font-family: "Montserrat", sans-serif;
    position: relative;
  }
  .card {
    position: absolute;
    top: 252px;
    width: 520px;
    height: 297px;
    box-shadow: 0 10px 28px var(--shadow);
    overflow: hidden;
  }
  .card-front { left: 50px; background: var(--ink); }
  .card-back { left: 630px; background: var(--paper); }

  .wordmark {
    display: flex;
    align-items: center;
    gap: 10px;
    font-weight: 800;
    letter-spacing: 1px;
    line-height: 1;
    white-space: nowrap;
  }
  .wordmark-square {
    width: 14px;
    height: 14px;
    background: var(--accent);
    flex: none;
  }
  .card-front .wordmark {
    position: absolute;
    left: 50%;
    top: 50%;
    transform: translate(-50%, -50%);
    font-size: 58px;
    color: var(--paper);
  }
  .card-front .wordmark-square { width: 18px; height: 18px; }
  .card-back .wordmark {
    position: absolute;
    right: 34px;
    top: 44px;
    font-size: 44px;
    color: var(--ink);
  }

  .holder {
    position: absolute;
    left: 34px;
    top: 178px;
    font-size: 15px;
    color: var(--accent);
  }
  .holder-name { font-weight: 700; letter-spacing: 0.5px; }
  .holder-role { color: var(--muted); font-weight: 300; }

  .contact {
    position: absolute;
    left: 34px;
    top: 208px;
    display: flex;
    align-items: center;
    gap: 8px;
    font-size: 12px;
    font-weight: 300;
    color: var(--muted);
    white-space: nowrap;
  }
  .contact-item { display: flex; align-items: center; gap: 5px; }
  .contact-sep { color: var(--accent); }
  .contact svg { width: 12px; height: 12px; fill: var(--ink); }

  .rule {
    position: absolute;
    left: 34px;
    right: 34px;
    top: 236px;
    height: 1px;
    background: var(--accent);
  }
</style>
</head>
<body>
  <section class="card card-front">
    <div class="wordmark"><span class="wordmark-square"></span>BREVANE</div>
  </section>

  <section class="card card-back">
    <div class="wordmark"><span class="wordmark-square"></span>BREVANE</div>

    <p class="holder"><span class="holder-name">MARK DALTON |</span> <span class="holder-role">Director</span></p>

    <div class="contact">
      <span class="contact-item">
        <svg viewBox="0 0 24 24" aria-hidden="true"><path d="M6.6 10.8a15 15 0 0 0 6.6 6.6l2.2-2.2c.3-.3.7-.4 1-.2 1.1.4 2.3.6 3.6.6.6 0 1 .4 1 1V20c0 .6-.4 1-1 1A17 17 0 0 1 3 4c0-.6.4-1 1-1h3.5c.6 0 1 .4 1 1 0 1.3.2 2.5.6 3.6.1.3 0 .7-.2 1z"/></svg>
        415-555-0182
      </span>
      <span class="contact-sep">|</span>
      <span class="contact-item">
        <svg viewBox="0 0 24 24" aria-hidden="true"><path d="M2 5h20v14H2zm2 2v.5l8 5 8-5V7l-8 5z"/></svg>
        info@brevane.com
      </span>
      <span class="contact-sep">|</span>
      <span class="contact-item">
        <svg viewBox="0 0 24 24" aria-hidden="true"><path d="M12 2a7 7 0 0 0-7 7c0 5 7 13 7 13s7-8 7-13a7 7 0 0 0-7-7zm0 9.5A2.5 2.5 0 1 1 12 6.5a2.5 2.5 0 0 1 0 5z"/></svg>
        12 harbor lane, unit 04
      </span>
    </div>

    <div class="rule"></div>
  </section>
</body>
</html>
```